CD Cover Design Project

Something very cool but simple. I need front, back, sleeve and disc. Disc I would like to have the old piano on from the pictures.

Target Market(s)

Fans, Music industry

Requirements
Must have
• Must have disc with piano keys on it. Please use the back photo for the piano keys. Thanks

All the text

Back:
Honestly

1. Tearin' Up

2. Her Coat Of Blue

3. Slow To Mend

4. Road We Wandered Down (Acoustic)

disc:
Renella Calloway

Honestly

Tearin' Up

Her Coat Of Blue

Slow To Mend

Road We Wandered Down (Acoustic)

Left Side:

Short Bio

A big thanks to my Mom, Sister and Dad. Also to Dewey Farnum, Grady Pemberton (mixes), Lyle Dorsey, Wren B. Dorinda Pruitt, Roy Quimby, Maxine Caldwell, Glen Ostrander, Dean Whitmore, Luther Vosslingen, Wade Prichett,Hal Ungerman, Loretta Pavlik, Ray Dunaway, and all my Backer Tunes supporters. I couldn't have done it without you.

Tearin' Up written by Pruitt and Calloway. Her Coat Of Blue written by Calloway and Hargrove, Slow To Mend written by Calloway
and Road We Wandered Down written by Calloway and Bramlett.

Right side:photo
Nice to have
• I would like to use the middle shot with the red dress if possible but not sure it's large enough. If not please use the other middle shot with the colors shirt and the mandolin. Thanks
Should not have
• Not too dark. Not to blocky.. Inclosed is something done this week that I don't like. Bad fonts and no graphics.

```html
<!DOCTYPE html>
<html lang="en">
<head>
<meta charset="utf-8">
<title>Renella Calloway – Honestly – Disc</title>
<link rel="stylesheet" href="https://fonts.googleapis.com/css2?family=Bodoni+Moda:wght@400;500&family=Great+Vibes&display=swap">
<style>
  :root {
    --page: #ffffff;
    --disc: #1f0f18;
    --disc-soft: #2a1621;
    --disc-edge: #160a11;
    --hub: #5a4852;
    --hub-light: #6e5c66;
    --rim: #c9d6d8;
    --gold: #cfc48c;
    --teal: #3fa99a;
    --label-text: #e9e4ea;
  }
  html, body {
    margin: 0;
    padding: 0;
    width: 1200px;
    height: 1104px;
    overflow: hidden;
    background: var(--page);
  }
  .disc-art {
    display: block;
    width: 1200px;
    height: 1104px;
  }
  .artist-name {
    font-family: "Bodoni Moda", serif;
    font-weight: 400;
    font-size: 78px;
    fill: var(--gold);
    letter-spacing: 3px;
  }
  .album-title {
    font-family: "Great Vibes", cursive;
    font-size: 108px;
    fill: var(--teal);
  }
  .track-list {
    font-family: "Bodoni Moda", serif;
    font-size: 14px;
    fill: var(--gold);
    letter-spacing: 0.5px;
  }
  .label-name {
    font-family: "Bodoni Moda", serif;
    font-weight: 500;
    font-size: 16px;
    fill: var(--label-text);
    letter-spacing: 1px;
  }
</style>
</head>
<body>
<svg class="disc-art" viewBox="0 0 1200 1104" xmlns="http://www.w3.org/2000/svg">
  <defs>
    <radialGradient id="hubGlow" cx="50%" cy="50%" r="50%">
      <stop offset="0%" stop-color="var(--hub-light)"/>
      <stop offset="80%" stop-color="var(--hub)"/>
      <stop offset="100%" stop-color="var(--disc)"/>
    </radialGradient>
    <linearGradient id="pianoTone" x1="0" y1="0" x2="1" y2="1">
      <stop offset="0%" stop-color="var(--disc-soft)"/>
      <stop offset="55%" stop-color="var(--disc)"/>
      <stop offset="100%" stop-color="var(--disc-edge)"/>
    </linearGradient>
    <path id="trackArc" d="M722,93 A465,465 0 0 1 1051,690"/>
  </defs>

  <!-- disc body -->
  <circle class="disc-rim" cx="594" cy="544" r="506" fill="var(--rim)"/>
  <circle class="disc-face" cx="594" cy="544" r="499" fill="url(#pianoTone)" stroke="var(--disc-edge)" stroke-width="2"
          role="img" aria-label="Toned photograph of old piano keys across the disc face"/>

  <!-- centre hub -->
  <circle class="disc-hub" cx="594" cy="544" r="146" fill="url(#hubGlow)"/>
  <circle class="disc-hole" cx="594" cy="544" r="63" fill="var(--page)"/>

  <!-- artist -->
  <text class="artist-name" x="605" y="275" text-anchor="middle">RENELLA</text>
  <text class="artist-name" x="605" y="366" text-anchor="middle">CALLOWAY</text>

  <!-- track list along the edge -->
  <text class="track-list">
    <textPath href="#trackArc" xml:space="preserve">1 Tearin' Up    2 Her Coat Of Blue    3 Slow To Mend    4 Road We Wandered Down (Acoustic)</textPath>
  </text>

  <!-- label -->
  <text class="label-name" x="116" y="549">NOVA CREST RECORDS</text>

  <!-- album title -->
  <text class="album-title" x="588" y="830" text-anchor="middle">Honestly</text>
</svg>
</body>
</html>
```